Selvin: A Friday night in the Prophetic Flyer

We are holding 2 Friday night events, one on 10/25/19 and the other on 11/29/19.
The time frame is 6:30pm-9:00pm. These services will be a time of prayer/healing for the sick and will be prophetic as well. (There will be prophets prophesying over people)

The event is called: Selvin: A Friday night in the Prophetic
The flyer should also include the phrase/excerpt: "And they prophesied also".

Keywords/Phrases: Prophetic, Healing, Climbing in the Spirit, Higher level of Anointing...

Target Market(s)

those looking for healing, seeking a word from God

Colors

Designer to choose colors to be used in the design.

Requirements
Must have
• The event is called: Selvin: A Friday night in the Prophetic
• The flyer should also include the phrase/excerpt: "And they prophesied also".
• It must include the Tovik logo attached, either is fine, we have attached two different versions.
• It must have the dates, location, time
• Dates: October 25, 2019 and November 29, 2019
• Location: Hollard Community Center
• (Downtown Portland) 482 Wendle Street
• Portland, ME 04102
• Time: 6:30pm-9:00pm
• Contact Info: Tel. 207-555-3841
• email: contact@brimfield-hall.org
• web: www.tovik.org
Nice to have
• creativity in color scheme, the meaning of the word Selvin conveyed in a classy artistic way/design.
Should not have
• Crosses, pictures of churches

```html
<!DOCTYPE html>
<html lang="en">
<head>
<meta charset="utf-8">
<title>Selvin: A Friday Night in the Prophetic</title>
<link rel="stylesheet" href="https://fonts.googleapis.com/css2?family=Oswald:wght@400;500;600;700&family=Anton&family=Kaushan+Script&display=swap">
<style>
  :root {
    --ink: #141414;
    --ember: #f7941d;
    --ember-deep: #d9650b;
    --white: #ffffff;
  }
  * { margin: 0; padding: 0; box-sizing: border-box; }
  html, body { width: 857px; height: 1200px; overflow: hidden; background: var(--ink); }
  .flyer {
    position: relative;
    width: 857px;
    height: 1200px;
    overflow: hidden;
    background: var(--ink);
    font-family: "Oswald", sans-serif;
    color: var(--white);
  }
  .smoke {
    position: absolute;
    inset: 0;
    background:
      radial-gradient(ellipse 220px 320px at 40px 260px, rgba(247,148,29,.55), transparent 70%),
      radial-gradient(ellipse 200px 260px at 830px 200px, rgba(247,148,29,.5), transparent 70%),
      radial-gradient(ellipse 180px 240px at 20px 620px, rgba(217,101,11,.45), transparent 70%),
      radial-gradient(ellipse 200px 260px at 850px 600px, rgba(217,101,11,.4), transparent 70%);
  }
  .photo {
    position: absolute;
    left: 150px;
    top: 230px;
    width: 557px;
    height: 420px;
    background: radial-gradient(ellipse at 50% 40%, #8a8a8a 0%, #4a4a4a 45%, var(--ink) 80%);
  }
  .frame {
    position: absolute;
    left: 24px; top: 24px; right: 24px; bottom: 24px;
    border: 3px solid var(--ember);
  }
  .centered { position: absolute; left: 0; width: 100%; text-align: center; line-height: 1; display: block; }
  .event-name {
    top: 36px;
    font-family: "Anton", sans-serif;
    font-size: 38px;
    letter-spacing: 3px;
    color: var(--ember);
  }
  .headline {
    top: 84px;
    font-family: "Anton", sans-serif;
    font-size: 74px;
    letter-spacing: 1px;
  }
  .headline-script {
    top: 164px;
    font-family: "Kaushan Script", cursive;
    font-size: 50px;
  }
  .date { position: absolute; top: 664px; line-height: 1; }
  .date--oct { left: 110px; text-align: left; }
  .date--nov { right: 100px; text-align: right; }
  .date-month { font-family: "Anton", sans-serif; font-size: 40px; letter-spacing: 2px; }
  .date-day { font-family: "Anton", sans-serif; font-size: 44px; color: var(--ember); margin-top: 8px; }
  .scripture {
    position: absolute;
    top: 660px; left: 328px; width: 200px;
    text-align: center;
    font-family: "Anton", sans-serif;
    line-height: 1;
  }
  .scripture-lead { font-size: 34px; color: var(--ember); }
  .scripture-rest { font-size: 23px; margin-top: 2px; }
  .time { top: 808px; font-family: "Anton", sans-serif; font-size: 34px; letter-spacing: 1px; }
  .keywords {
    top: 872px;
    font-weight: 700;
    font-size: 26px;
    color: var(--ember);
    letter-spacing: .5px;
  }
  .anointing {
    top: 910px;
    font-family: "Anton", sans-serif;
    font-size: 38px;
    letter-spacing: 1px;
  }
  .location {
    top: 958px;
    font-weight: 500;
    font-size: 18px;
    letter-spacing: .5px;
  }
  .brand {
    position: absolute;
    left: 70px; top: 1040px;
    display: flex; align-items: center; gap: 10px;
    font-family: "Anton", sans-serif;
    font-size: 40px;
    letter-spacing: 2px;
    line-height: 1;
    color: var(--white);
  }
  .brand-dot { width: 18px; height: 18px; border-radius: 50%; background: var(--ember); }
  .contact { position: absolute; left: 330px; top: 996px; width: 470px; text-align: center; line-height: 1; }
  .contact-call { font-weight: 600; font-size: 26px; letter-spacing: 1px; }
  .contact-tel { font-family: "Anton", sans-serif; font-size: 40px; color: var(--ember); margin-top: 8px; letter-spacing: 1px; }
  .contact-mail { display: flex; justify-content: center; align-items: center; gap: 10px; font-size: 20px; font-weight: 500; margin-top: 8px; text-transform: uppercase; }
  .contact-web { font-family: "Anton", sans-serif; font-size: 36px; color: var(--ember); margin-top: 8px; letter-spacing: 1px; }
</style>
</head>
<body>
<main class="flyer">
  <div class="smoke" role="img" aria-label="Orange smoke drifting along the edges"></div>
  <div class="photo" role="img" aria-label="Black and white photograph of a man praying with clasped hands"></div>
  <div class="frame"></div>

  <h1>
    <span class="centered event-name">SELVIN</span>
    <span class="centered headline">A FRIDAY NIGHT</span>
    <span class="centered headline-script">in the Prophetic</span>
  </h1>

  <div class="date date--oct">
    <div class="date-month">OCTOBER</div>
    <div class="date-day">2019. 25</div>
  </div>
  <div class="scripture">
    <div class="scripture-lead">AND</div>
    <div class="scripture-rest">THEY<br>PROPHESIED<br>ALSO</div>
  </div>
  <div class="date date--nov">
    <div class="date-month">NOVEMBER</div>
    <div class="date-day">2019 . 29</div>
  </div>

  <p class="centered time">6:30PM-9:00PM</p>
  <p class="centered keywords">PROPHETIC, HEALING, CLIMBING IN THE SPIRIT</p>
  <p class="centered anointing">HIGHER LEVEL OF ANOINTING...</p>
  <p class="centered location">HOLLARD COMMUNITY CENTER · 482 WENDLE STREET · PORTLAND, ME 04102</p>

  <div class="brand"><span class="brand-dot"></span>TOVIK</div>

  <div class="contact">
    <p class="contact-call">FOR MORE INFO CALL US NOW</p>
    <p class="contact-tel">TEL. 207-555-3841</p>
    <p class="contact-mail">
      <svg width="24" height="17" viewBox="0 0 24 17" aria-hidden="true">
        <rect x="1" y="1" width="22" height="15" fill="none" stroke="#ffffff" stroke-width="2"/>
        <polyline points="1,1 12,10 23,1" fill="none" stroke="#ffffff" stroke-width="2"/>
      </svg>
      contact@brimfield-hall.org
    </p>
    <p class="contact-web">WWW.TOVIK.ORG</p>
  </div>
</main>
</body>
</html>
```